Webdesign für Getränkelogistik & Full-Service-Partner bei Events
Zielgruppe
Getränkelogistiker und Full-Service-Partner bei Events
Zielgruppe: Getränke-EinzelHändler; Veranstalter von Events und privaten Feiern
Aufgabenstellung
- soll „Frische“ und „Moderne“ vermitteln, ohne eine Getränkeart in den Vordergrund zu rücken
- soll von den Farben her gut zum Logo passen (siehe Anlagen)
- Slider wäre wünschenswert
- Slogan 'Wir freuen uns auf Sie!'

```html
<!DOCTYPE html>
<html lang="de">
<head>
<meta charset="utf-8">
<title>Getränke Rahnfeld GmbH – Startseite</title>
<link href="https://fonts.googleapis.com/css2?family=Open+Sans:wght@400;600;700&family=Playfair+Display:wght@700&display=swap" rel="stylesheet">
<style>
  :root{
    --green:#17604f;
    --green-dark:#135446;
    --yellow:#f6c400;
    --yellow-light:#fadc2a;
    --text:#333;
    --line:#cfcfcf;
    --white:#fff;
  }
  *{margin:0;padding:0;box-sizing:border-box}
  html,body{width:1146px;height:1200px;overflow:hidden;background:var(--white)}
  body{position:relative;font-family:"Open Sans",Arial,sans-serif;color:var(--text)}
  .brand{position:absolute;top:26px;left:0;width:1146px;display:flex;justify-content:center;align-items:center;gap:10px}
  .brand-dot{width:30px;height:30px;border-radius:50%;background:var(--yellow)}
  .brand-name{font-family:"Open Sans",Arial,sans-serif;font-weight:700;font-size:22px;color:var(--green)}
  .nav{position:absolute;left:222px;top:90px;width:702px;height:47px;border-top:1px solid var(--line);border-bottom:1px solid var(--line);display:flex;justify-content:center;align-items:center;gap:28px;font-size:11px;color:#444}
  .nav .active{font-weight:700;color:var(--green)}
  .hero{position:absolute;left:140px;top:154px;width:865px;height:421px;background:linear-gradient(110deg,#5a6f86 0%,#c07a3e 30%,#e9a12f 55%,#f7c35a 75%,#f2e2c0 100%)}
  .hero-quote{position:absolute;left:140px;top:389px;width:364px;height:122px;background:var(--green);padding:16px 0 0 82px;font-family:"Playfair Display",Georgia,serif;font-weight:700;font-size:38px;line-height:43px;color:var(--yellow)}
  .hotline{position:absolute;left:994px;top:172px;width:152px;height:57px;background:var(--yellow);padding:8px 0 0 11px}
  .hotline small{display:block;font-size:11.5px;color:#333}
  .hotline strong{display:block;font-size:19.5px;font-weight:700;color:var(--green);line-height:24px}
  .beer{position:absolute;left:139px;top:900px;width:867px;height:300px;background:linear-gradient(180deg,#fff 0%,#eceded 26%,#e9e9e7 33%,#f6c800 36%,#f7c900 60%,#fadd10 100%)}
  .services{position:absolute;left:222px;top:645px;display:flex;gap:18px}
  .service{width:162px;position:relative}
  .service-label{font-size:10px;font-weight:700;color:var(--yellow);letter-spacing:.3px}
  .service-rule{width:30px;height:1px;background:#aaa;margin:11px 0 0}
  .service-title{font-family:"Playfair Display",Georgia,serif;font-weight:700;font-size:23px;color:var(--green);margin-top:15px}
  .service-text{font-size:10.5px;line-height:16.6px;margin-top:20px;height:80px}
  .service-photo{display:block;width:162px;height:111px;margin-top:1px}
  .service-more{display:block;text-align:right;font-size:11px;font-weight:700;color:var(--green);text-decoration:underline;margin-top:17px}
  .footer-col{position:absolute;top:1064px;font-size:11px;line-height:21.5px;color:#333}
  .footer-col svg{position:absolute;left:-20px}
  .footer-list{list-style:none}
  .footer-list li::before{content:"• "}
  .footer-rule{position:absolute;left:222px;top:1161px;width:702px;height:1px;background:#555}
  .copyright{position:absolute;top:1173px;left:0;width:1146px;text-align:center;font-size:11px;color:#333}
</style>
</head>
<body>
  <header class="brand">
    <span class="brand-dot"></span>
    <span class="brand-name">Getränke Rahnfeld GmbH</span>
  </header>

  <nav class="nav">
    <span class="active">Home</span><span>Unternehmen</span><span>Team</span><span>Großhandel</span><span>Rund um Ihr Event</span><span>Karriere</span><span>Kontakt</span>
  </nav>

  <div class="hero" role="img" aria-label="Freunde stoßen im Sonnenlicht mit Getränkeflaschen an"></div>
  <div class="hero-quote">“Wir freuen uns auf Sie!”</div>

  <aside class="hotline"><small>Bestell-Hotline:</small><strong>0371 4455 210</strong></aside>

  <div class="beer" role="img" aria-label="Hintergrund mit Schaum und goldenem Getränk"></div>

  <section class="services">
    <article class="service">
      <div class="service-label">SERVICE 01</div><div class="service-rule"></div>
      <h2 class="service-title">Für Ihr Event</h2>
      <p class="service-text">Dies ist ein Typoblindtext. An ihm kann man sehen, ob alle Buchstaben da sind und wie sie aussehen.</p>
      <div class="service-photo" role="img" aria-label="Festlich dekoriertes Eventzelt im Freien" style="background:linear-gradient(160deg,#2b3fb8,#8fa3d8 45%,#e8e8ea 70%,#9a9184)"></div>
      <a class="service-more">weiterlesen</a>
    </article>
    <article class="service">
      <div class="service-label">SERVICE 02</div><div class="service-rule"></div>
      <h2 class="service-title">Großhandel</h2>
      <p class="service-text">Dies ist ein Typoblindtext. An ihm kann man sehen, ob alle Buchstaben da sind und wie sie aussehen.</p>
      <div class="service-photo" role="img" aria-label="Reihe grüner Lieferwagen auf dem Hof" style="background:linear-gradient(180deg,#cfd3d6 0%,#c9c9b0 30%,#2f6d3d 45%,#1f4d2c 75%,#7c7e80 100%)"></div>
      <a class="service-more">weiterlesen</a>
    </article>
    <article class="service">
      <div class="service-label">SERVICE 03</div><div class="service-rule"></div>
      <h2 class="service-title">Unternehmen</h2>
      <p class="service-text">Dies ist ein Typoblindtext. An ihm kann man sehen, ob alle Buchstaben da sind und wie sie aussehen.</p>
      <div class="service-photo" role="img" aria-label="Geschäftsführer lehnt an einem Treppengeländer" style="background:linear-gradient(120deg,#6d7470,#d9ddde 45%,#b9bcbf 70%,#55595a)"></div>
      <a class="service-more">weiterlesen</a>
    </article>
    <article class="service">
      <div class="service-label">SERVICE 04</div><div class="service-rule"></div>
      <h2 class="service-title">Team</h2>
      <p class="service-text">Dies ist ein Typoblindtext. An ihm kann man sehen, ob alle Buchstaben da sind und wie sie aussehen.</p>
      <div class="service-photo" role="img" aria-label="Gesamtes Team vor der Lagerhalle" style="background:linear-gradient(180deg,#c9c21a 0%,#3a3f3c 20%,#7a7f7b 50%,#2f5a3a 75%,#8a8b88 100%)"></div>
      <a class="service-more">weiterlesen</a>
    </article>
  </section>

  <div class="footer-col" style="left:241px">
    <svg width="14" height="18" viewBox="0 0 14 18" style="top:2px"><path d="M7 0C3.1 0 0 3.1 0 7c0 5 7 11 7 11s7-6 7-11c0-3.9-3.1-7-7-7zm0 9.5A2.5 2.5 0 1 1 7 4.5a2.5 2.5 0 0 1 0 5z" fill="var(--green)"/></svg>
    Getränke Rahnfeld GmbH<br>Am Lindenhof 14<br>09120 Talheim
  </div>
  <div class="footer-col" style="left:487px">
    <svg width="16" height="16" viewBox="0 0 16 16" style="top:1px;left:-23px"><path d="M3.5 0.5l3 3-1.8 2.2c1 2 2.6 3.6 4.6 4.6l2.2-1.8 3 3-2 2.5C7 13.5 2.5 9 0.5 2.5z" fill="var(--green)"/></svg>
    Telefon: +49 371 4455 210<br>Telefax: +49 371 4455 211<br>
    <svg width="16" height="12" viewBox="0 0 16 12" style="top:49px;left:-23px"><rect width="16" height="12" rx="1" fill="var(--green)"/><path d="M1 1.5l7 5 7-5" stroke="var(--yellow)" stroke-width="1.4" fill="none"/></svg>
    info(at)getraenke-rahnfeld.de
  </div>
  <ul class="footer-col footer-list" style="left:701px;top:1062px">
    <li>Downloads</li><li>Kontakt</li><li>Impressum/Datenschutz</li><li>AGB</li>
  </ul>
  <div class="footer-rule"></div>
  <div class="copyright">© 2020 getraenke-rahnfeld.de</div>
</body>
</html>
```